arts & crafts

I collect old plates & make them into serving plates for cakes, afternoon teas, special occasions, weddings, parties, bridal showers. cake competitions, displays in bakeries.

Contact Information for Business Card

Tulips Turn Gold
giving old plates a new life
Ph 0412873905
info@ tulipsturngold.com.au
www.tulipsturngold.com.au
facebook
Craftly

```html
<!DOCTYPE html>
<html lang="en">
<head>
<meta charset="utf-8">
<title>Tulips Turn Gold – Business Card</title>
<link href="https://fonts.googleapis.com/css2?family=Aladin&display=swap" rel="stylesheet">
<style>
  :root {
    --backdrop: #a8a19e;
    --card: #ffffff;
    --facet-light: #f4f4f4;
    --facet-mid: #dcdcdc;
    --band-brown: #76502d;
    --halo-blue: #b9dce8;
    --plate-rose: #b8647a;
    --plate-deep: #8e3d55;
    --maroon: #8e2a4f;
    --teal: #6fb3c0;
    --brown: #76502d;
    --ink: #111111;
  }
  * { margin: 0; padding: 0; box-sizing: border-box; }
  html, body { width: 1200px; height: 856px; overflow: hidden; }
  body { background: var(--backdrop); position: relative; font-family: "Aladin", cursive; }

  .business-card {
    position: absolute; left: 100px; top: 128px;
    width: 1000px; height: 600px;
    background: var(--card);
    border-radius: 44px;
    overflow: hidden;
  }
  .facet-field {
    position: absolute; left: 0; top: 0; width: 640px; height: 100%;
    background: linear-gradient(90deg, var(--facet-mid) 0%, var(--facet-light) 55%, var(--card) 100%);
  }
  .brown-band {
    position: absolute; left: 178px; top: 0; width: 195px; height: 100%;
    background: var(--band-brown);
  }
  .plate-halo {
    position: absolute; left: 36px; top: 68px; width: 474px; height: 474px;
    border-radius: 50%;
    background: radial-gradient(circle, #d3ebf2 0%, var(--halo-blue) 100%);
  }
  .plate-photo {
    position: absolute; left: 73px; top: 105px; width: 400px; height: 400px;
    border-radius: 50%;
    background: radial-gradient(circle, var(--plate-rose) 0%, #c77e91 60%, var(--plate-deep) 100%);
  }

  .card-details {
    position: absolute; right: 60px; top: 62px;
    text-align: right; line-height: 1;
  }
  .brand-name {
    color: var(--maroon); font-size: 72px; line-height: 0.92;
    margin-bottom: 44px;
  }
  .business-name { color: var(--brown); font-size: 28px; margin-bottom: 6px; }
  .tagline { color: var(--ink); font-size: 32px; margin-bottom: 38px; }
  .contact-line { font-size: 29px; margin-bottom: 6px; }
  .phone { color: var(--brown); margin-bottom: 10px; }
  .email { color: var(--maroon); }
  .website { color: var(--teal); }
  .handle { display: flex; justify-content: flex-end; align-items: center; gap: 14px; }
  .handle.facebook { color: var(--maroon); }
  .handle.craftly { color: var(--teal); }
  .social-square {
    width: 22px; height: 22px; border-radius: 4px; background: var(--brown);
  }
</style>
</head>
<body>
  <div class="business-card">
    <div class="facet-field" role="img" aria-label="Soft grey low-poly faceted background pattern"></div>
    <div class="brown-band"></div>
    <div class="plate-halo" role="img" aria-label="Pale blue painted wood backdrop behind the plate"></div>
    <div class="plate-photo" role="img" aria-label="Photo of an embossed pink vintage plate holding a slice of chocolate cake"></div>

    <div class="card-details">
      <div class="brand-name">Tulips<br>Turn Gold</div>
      <div class="business-name">Tulips Turn Gold</div>
      <div class="tagline">giving old plates a new life</div>
      <div class="contact-line phone">0412873905</div>
      <div class="contact-line email">info@ tulipsturngold.com.au</div>
      <div class="contact-line website">www.tulipsturngold.com.au</div>
      <div class="contact-line handle facebook">TulipsTurnGold <span class="social-square"></span></div>
      <div class="contact-line handle craftly">TulipsTurnGold <span class="social-square"></span></div>
    </div>
  </div>
</body>
</html>
```